Criação de Papelaria (6 itens) para Roupas, Jóias & Assessorios
A empresa queria:
" Nossa loja nao é sapataria,ela tem mais um estilo boutique, ou seja é um tamanho menor,no entanto nossos preços sao voltados para os publicos B e C. Resumindo é uma loja que parece ser cara pela estrutura,mas tem preços acessíveis. Sem deixar cair a qualidade,nem a beleza. Gostamos de dizer que temos produtos diferenciados, ou seja, nosso gosto é peculiar, as clientes se encantam pelas coleçoes. Temos aparência de franquia, apesar de nao sermos. "

```html
<!DOCTYPE html>
<html lang="pt-BR">
<head>
<meta charset="utf-8">
<title>Lívia Marchetti – Cartão de Visita</title>
<link rel="stylesheet" href="https://fonts.googleapis.com/css2?family=Cinzel:wght@500&family=Roboto:wght@400&display=swap">
<style>
  :root {
    --page: #f2f2f2;
    --card-black: #231f20;
    --pink: #e0157f;
    --pink-deep: #b80d66;
    --silver: #d9d9d9;
    --oval: #2a2627;
    --text-light: #ffffff;
  }
  * { margin: 0; padding: 0; box-sizing: border-box; }
  html, body { width: 1200px; height: 1200px; overflow: hidden; background: var(--page); }
  .sheet {
    width: 1200px; height: 1200px;
    display: flex; flex-direction: column; align-items: center; justify-content: center; gap: 60px;
  }
  .card {
    position: relative; width: 900px; height: 500px;
    background: var(--card-black);
    box-shadow: 0 6px 18px rgba(0,0,0,.18);
    overflow: hidden;
    font-family: "Roboto", sans-serif; color: var(--text-light);
  }
  .band {
    position: absolute; left: 0; right: 0;
    background: linear-gradient(90deg, var(--pink-deep), var(--pink) 30%, var(--pink) 70%, var(--pink-deep));
  }
  .card--front .band { top: 180px; height: 140px; }
  .card--back .band { top: 200px; height: 160px; }

  .emblem {
    position: absolute; left: 50%; transform: translateX(-50%);
    display: flex; flex-direction: column; align-items: center;
  }
  .card--front .emblem { top: 88px; }
  .card--back .emblem { top: 30px; transform: translateX(-50%) scale(.62); transform-origin: top center; }
  .flourish { width: 170px; height: 42px; background: var(--silver); opacity: .18; border-radius: 20px; }
  .oval {
    width: 440px; height: 190px; margin: 8px 0;
    border-radius: 50%;
    background: var(--oval);
    border: 4px solid var(--silver);
    display: flex; align-items: center; justify-content: center;
  }
  .brand-name {
    font-family: "Cinzel", serif; font-weight: 500; font-size: 40px; letter-spacing: 1px;
    color: var(--text-light);
  }

  .holder {
    position: absolute; left: 90px; top: 236px;
    font-size: 20px; line-height: 1.5;
  }
  .holder .name { margin-bottom: 18px; }

  .contacts {
    position: absolute; right: 60px; top: 190px;
    list-style: none; font-size: 17px; text-align: right;
  }
  .contacts li { display: flex; align-items: center; justify-content: flex-end; gap: 12px; height: 48px; }
  .contacts svg { width: 22px; height: 22px; flex: none; }
</style>
</head>
<body>
<main class="sheet">

  <section class="card card--front" aria-label="Frente do cartão">
    <div class="band" role="img" aria-label="Faixa rosa com padrão ondulado sutil"></div>
    <div class="emblem">
      <div class="flourish" role="img" aria-label="Ornamento prateado superior"></div>
      <div class="oval"><span class="brand-name">LÍVIA MARCHETTI</span></div>
      <div class="flourish" role="img" aria-label="Ornamento prateado inferior"></div>
    </div>
  </section>

  <section class="card card--back" aria-label="Verso do cartão">
    <div class="band" role="img" aria-label="Faixa rosa com padrão ondulado sutil"></div>
    <div class="emblem">
      <div class="flourish" role="img" aria-label="Ornamento prateado superior"></div>
      <div class="oval"><span class="brand-name">LÍVIA MARCHETTI</span></div>
      <div class="flourish" role="img" aria-label="Ornamento prateado inferior"></div>
    </div>

    <div class="holder">
      <p class="name">Nome</p>
      <p>R. Seu endereço- 000</p>
      <p>Cidade nova AM</p>
    </div>

    <ul class="contacts">
      <li>00 0000-0000
        <svg viewBox="0 0 24 24" aria-hidden="true"><path fill="#fff" d="M6.6 10.8a15 15 0 0 0 6.6 6.6l2.2-2.2c.3-.3.7-.4 1-.2 1.1.4 2.3.6 3.6.6.6 0 1 .4 1 1V20c0 .6-.4 1-1 1A17 17 0 0 1 3 4c0-.6.4-1 1-1h3.5c.6 0 1 .4 1 1 0 1.3.2 2.5.6 3.6.1.3 0 .7-.2 1z"/></svg>
      </li>
      <li>livia@liviamarchetti.com
        <svg viewBox="0 0 24 24" aria-hidden="true"><rect x="2.5" y="5" width="19" height="14" fill="none" stroke="#fff" stroke-width="1.8"/><path d="M3 6l9 7 9-7" fill="none" stroke="#fff" stroke-width="1.8"/></svg>
      </li>
      <li>www.liviamarchetti.com.br
        <svg viewBox="0 0 24 24" aria-hidden="true"><rect x="3" y="3" width="18" height="18" rx="3" fill="#fff"/></svg>
      </li>
    </ul>
  </section>

</main>
</body>
</html>
```